Web Design Project

Looking for a simple, yet creative, small company website that can grow with me. The company name is Dralvo Creations and the first products will be branded as FlurinWarm warmers.

The first product I am selling are small reusable sodium acetate warming pads directed to two markets. 1) outdoor sporting/hunting activities and 2) spa/heat therapy. Three different sizes of warmers are currently availaible.

One differentiating aspect of our product is a custom designed neoprene insulating sleeve into which the warmer fits so that it stays warmer longer.

Looking for a website that is simple, easy to navigate and fun.

I would like to be able to sell items directly from website and direct to Voltmart as well.

I have a logo to base your ideas on.

Target Market(s)

Pictures of the first three products. Please incorporate.

Requirements
Must have
• selling cart
contact page
how they work
Nice to have
• product video, may be added later

```html
<!DOCTYPE html>
<html lang="en">
<head>
<meta charset="utf-8">
<title>FlurinWarm – How We Work</title>
<link rel="stylesheet" href="https://fonts.googleapis.com/css2?family=Source+Sans+3:wght@400;600&family=Arimo&display=swap">
<style>
:root{
  --page:#f3f3f3;
  --red:#b8232b;
  --red-dark:#8e1419;
  --red-light:#d23a40;
  --heading:#b3252c;
  --text:#444;
  --muted:#666;
  --link:#2a7bbf;
  --footer:#232323;
  --footer-text:#bdbdbd;
}
*{margin:0;padding:0;box-sizing:border-box}
html,body{width:1200px;height:832px;overflow:hidden}
body{background:var(--page);font-family:"Source Sans 3",sans-serif;color:var(--text);position:relative}

.brand{position:absolute;left:216px;top:22px;display:flex;align-items:center;gap:10px}
.brand-mark{width:56px;height:56px;background:var(--red);border-radius:10px}
.brand-name{font-size:34px;font-weight:600;color:#1c1c1c;letter-spacing:.5px}

.account-links{position:absolute;right:216px;top:31px;font-size:10.5px;color:#666;display:flex;gap:12px}
.account-links span.sep{color:#999}
.search{position:absolute;left:783px;top:56px;width:201px;height:24px;display:flex;border:1px solid #ccc;background:#fff}
.search-field{flex:1;font-size:9.5px;color:#888;padding:6px 14px}
.search-btn{width:24px;background:#b7b7b7;display:flex;align-items:center;justify-content:center}

.main-nav{position:absolute;left:216px;top:112px;width:768px;height:32px;display:flex;background:linear-gradient(#cc2d33,#a91e24)}
.main-nav a{width:96px;color:#fff;text-decoration:none;font-size:12.5px;display:flex;align-items:center;justify-content:center;border-right:1px solid #8f181d}
.main-nav a:last-child{border-right:none}
.main-nav a.active{background:linear-gradient(#b8262c,#8f171c)}

.content{position:absolute;left:216px;top:170px;width:465px}
.content h1{font-size:22px;font-weight:400;color:var(--heading);margin-bottom:6px}
.content h2{font-family:Arimo,sans-serif;font-size:14px;font-weight:400;color:var(--heading);margin:28px 0 15px}
.content p{font-family:Arimo,sans-serif;font-size:10.3px;line-height:17px;text-align:justify;margin-bottom:17px;color:#444}

.sidebar{position:absolute;left:734px;top:170px;width:250px}
.sidebar h3{font-size:22px;font-weight:400;color:var(--heading);margin-bottom:8px}
.service-tile{position:relative;width:248px;height:103px;margin-left:2px;border:1px solid #ccc;margin-bottom:25px;display:flex;align-items:flex-end;justify-content:center}
.service-tile.spa{background:linear-gradient(160deg,#e8e1d8,#b9a594 60%,#3a302a)}
.service-tile.outdoor{background:linear-gradient(180deg,#8d96a0,#c7cbce 55%,#a99f86)}
.service-tile span{color:#fff;font-size:15px;padding-bottom:8px}
.how-text{font-size:9px;line-height:15px;color:var(--muted);margin-left:2px}
.how-text p{margin-bottom:15px}
.how-text p.tight{margin-bottom:0}
.how-text a{color:var(--link);text-decoration:none}
.video{margin:4px 0 0 2px;width:248px;height:152px;border:2px solid #444;background:linear-gradient(135deg,#c9a89a,#7a5b50 55%,#3a2d28);position:relative}
.video-play{position:absolute;left:105px;top:64px;width:45px;height:28px;background:#8e1a1d;display:flex;align-items:center;justify-content:center}
.video-bar{position:absolute;left:0;right:0;bottom:0;height:15px;background:#1e1e1e;display:flex;align-items:center;gap:6px;padding:0 4px;font-size:6px;color:#aaa}
.video-track{flex:1;height:3px;background:#555;position:relative}
.video-track i{position:absolute;left:0;top:0;width:60%;height:3px;background:#ccc}

.site-footer{position:absolute;left:0;top:784px;width:1200px;height:48px;background:var(--footer);color:var(--footer-text);font-size:9.5px}
.site-footer .copy{position:absolute;left:215px;top:18px}
.site-footer .follow{position:absolute;right:216px;top:14px;display:flex;align-items:center;gap:4px}
.site-footer .follow span{margin-right:6px}
.social{width:15px;height:15px;border-radius:2px}
.social.s1{background:#3b5a99}.social.s2{background:#1e78b4}.social.s3{background:#e4762b}.social.s4{background:#c8302c}
</style>
</head>
<body>

<header>
  <div class="brand"><div class="brand-mark"></div><div class="brand-name">FlurinWarm</div></div>
  <nav class="account-links">
    <span>Login</span><span class="sep">:</span><span>My Account</span><span class="sep">:</span><span>My Shopping Cart ( 0 )</span><span class="sep">:</span><span>Check out</span>
  </nav>
  <div class="search">
    <div class="search-field">Search</div>
    <div class="search-btn">
      <svg width="10" height="10" viewBox="0 0 10 10"><circle cx="6" cy="4" r="3" fill="none" stroke="#fff" stroke-width="1.3"/><line x1="4" y1="6" x2="1" y2="9" stroke="#fff" stroke-width="1.5"/></svg>
    </div>
  </div>
  <nav class="main-nav">
    <a class="active">Home</a><a>About us</a><a>Services</a><a>Products</a><a>Heat Therapy</a><a>Spa</a><a>Testimonials</a><a>Contact</a>
  </nav>
</header>

<main class="content">
  <h1>How We Work</h1>
  <p>Lorem Ipsum is simply dummy text of the printing and typesetting industry. Lorem Ipsum has been the industry's standard dummy text ever since the 1500s, when an unknown printer took a galley of type and scrambled it to make a type specimen book. It has survived not only five centuries, but also the leap into electronic typesetting, remaining essentially unchanged. It was popularised in the 1960s with the release of Typevell sheets containing Lorem Ipsum passages, and more recently with desktop publishing software like Quillmark Layout including versions of Lorem Ipsum</p>
  <p>Contrary to popular belief, Lorem Ipsum is not simply random text. It has roots in a piece of classical Latin literature from 45 BC, making it over 2000 years old. Edwin Halloway, a Latin professor at Brackwood College in Virginia, looked up one of the more obscure Latin words, consectetur, from a Lorem Ipsum passage, and going through the cites of the word in classical literature, discovered the undoubtable source. Lorem Ipsum comes from sections 1.10.32 and 1.10.33 of "de Finibus Bonorum et Malorum" (The Extremes of Good and Evil) by Marcellus, written in 45 BC. This book is a treatise on the theory of ethics, very popular during the Renaissance. The first line of Lorem Ipsum, "Lorem ipsum dolor sit amet..", comes from a line in section 1.10.32.</p>
  <h2>Subheading</h2>
  <p>Contrary to popular belief, Lorem Ipsum is not simply random text. It has roots in a piece of classical Latin literature from 45 BC, making it over 2000 years old. Edwin Halloway, a Latin professor at Brackwood College in Virginia, looked up one of the more obscure Latin words, consectetur, from a Lorem Ipsum passage, and going through the cites of the word in classical literature, discovered the undoubtable source. Lorem Ipsum comes from sections 1.10.32 and 1.10.33 of "de Finibus Bonorum et Malorum" (The Extremes of Good and Evil) by Marcellus, written in 45 BC. This book is a treatise on the theory of ethics, very popular during the Renaissance. The first line of Lorem Ipsum, "Lorem ipsum dolor sit amet..", comes from a line in section 1.10.32.</p>
  <p>The standard chunk of Lorem Ipsum used since the 1500s is reproduced below for those interested. Sections 1.10.32 and 1.10.33 from "de Finibus Bonorum et Malorum" by Marcellus are also reproduced in their exact original form, accompanied by English versions from the 1914 translation by H. Ravenmoor.</p>
</main>

<aside class="sidebar">
  <h3>Our Services</h3>
  <div class="service-tile spa" role="img" aria-label="Photo of a woman relaxing during a spa heat therapy session"><span>Spa &amp; Heat Therapy</span></div>
  <div class="service-tile outdoor" role="img" aria-label="Photo of a hunter in the field under an open sky"><span>Outdoor Sporting &amp; Hunting</span></div>
  <h3 style="margin-top:-5px">How it works</h3>
  <div class="how-text">
    <p>Lorem ipsum dolor sit amet, consectetur adipisicing elit, sed do eiusmod tempor incididunt ut labore et dolore magna aliqua.</p>
    <p class="tight">Ut enim ad minim veniam, quis nostrud exercitation ullamco laboris nisi ut aliquip ex ea commodo consequat.</p>
    <a>Watch Video Below</a>
  </div>
  <div class="video" role="img" aria-label="Video still of warm stones placed on a back">
    <div class="video-play"><svg width="12" height="12" viewBox="0 0 12 12"><path d="M2 1 L11 6 L2 11 Z" fill="#fff"/></svg></div>
    <div class="video-bar">
      <svg width="6" height="6" viewBox="0 0 6 6"><path d="M0 0 L6 3 L0 6 Z" fill="#ccc"/></svg>
      <div class="video-track"><i></i></div>
      <span>1:02 / 2:00 HD</span>
    </div>
  </div>
</aside>

<footer class="site-footer">
  <div class="copy">Copyright © Nova Domains - All Rights Reserved. Privacy Policy | Terms &amp; Condition</div>
  <div class="follow"><span>Follow us on</span><div class="social s1"></div><div class="social s2"></div><div class="social s3"></div><div class="social s4"></div></div>
</footer>

</body>
</html>
```